India March 15 Flyer

I would like a A4 Flyer made.
Very similair to attached file but the following changes
Name would be Wander India Fabric & Flavour Journey

Cost $6995.00pp
16days fully escorted
Breakfast & Dinner included for 15days
Tour Departs Auckland 15th March 2015

Take out anything that is associated to Corbel Globe Voyages and it should be KiwiTrip Agents (attached) file for this.
Also no address just phone no's which is
09 358 6172
021637294
maren@kiwitripagents.example.nz
KiwiTrip Agents Support Office:
Level 4, Quorn Plaza House, 3-21 Bellamy Rd,
Palmerston North 4410
Web:www.kiwitripagents.example.nz
Under conditions take out Corbel Globe Voyages and put in KiwiTrip Agents and prices correct as at 20August 2014.
Under Conditions please change $400 deposit to $500 deposit pp.
Under Conditions: Price is Share Twin. Please advise if you want a single supplement cost.
I have attached a flyer that was done for me when i did the last tour. So this will give you an idea.
Also have attached the current itinerary that we will be doing for the March 2015 tour.
Hope this is enough information
Updates

Hello, Please do not forget to do the back of the flyer. dont put in itinerary but maybe a picture of the region that we are traveling and the Terms and Conditions which is so important. Thanks

I have noticed that the designs comming through dont have fully escorted by Maren Thistle which is a part of the brief with the flyer I included. Also return flights etc. Everything that was on the orginal flyer needs to include all of this except the Corbel Globe Voyages.

as this is a textile and culinary tour i would like to see pictures of textiles and food, as well as the normal pictures of India. I only seem to be getting elephant, taj extra but need to show the tour i am selling. Many thanks

Please re read the brief as i have made the required changes on this. IE: Price is now changed as well as some Terms and Conditions

Requirements
Must have
• About Maren Thistle
Nice to have
• Pictures of Textiles and Culinerary as well as monuments

```html
<!DOCTYPE html>
<html lang="en">
<head>
<meta charset="utf-8">
<title>Wander India Fabric &amp; Flavour Journey – Flyer</title>
<link href="https://fonts.googleapis.com/css2?family=Carlito:ital,wght@0,400;0,700;1,400;1,700&display=swap" rel="stylesheet">
<style>
:root{
  --green:#2bb04a;
  --green-dark:#1f9a3c;
  --green-light:#47bd5f;
  --orange:#f7a22c;
  --gold:#f4c430;
  --white:#ffffff;
  --ink:#1c1c1c;
  --backdrop:#e9e6e1;
}
*{margin:0;padding:0;box-sizing:border-box}
html,body{width:1200px;height:800px;overflow:hidden}
body{background:var(--backdrop);font-family:"Carlito",Calibri,sans-serif;color:var(--ink);position:relative}

/* front page */
.front{position:absolute;left:35px;top:28px;width:567px;height:744px;background:var(--green);border-radius:0 40px 0 0}
.hero{position:absolute;left:20px;top:20px;width:485px;height:450px;border-radius:70px 40px 0 0;
  background:linear-gradient(180deg,#3f5a2e 0%,#57763f 30%,#8a8d74 55%,#c9762e 72%,#7a7362 88%,#5a5545 100%)}
.hero-title{position:absolute;left:55px;top:97px;width:405px;height:103px;background:var(--green);
  border-radius:18px 18px 18px 0;color:var(--orange);font-weight:700;font-size:34px;line-height:47px;text-align:center;padding-top:5px}
.hero-title::after{content:"";position:absolute;right:0;bottom:-20px;border-left:22px solid transparent;border-top:20px solid var(--green-dark)}
.intro{position:absolute;left:27px;top:486px;width:218px;color:var(--white);font-size:12px;line-height:20px}
.intro em{font-weight:700}
.front-foot{position:absolute;left:20px;top:570px;width:485px;height:144px;background:var(--white);border-radius:0 0 0 40px}
.offer{position:absolute;left:255px;top:420px;width:222px;height:200px;background:var(--green);border-radius:22px 0 0 0;z-index:2}
.price{color:var(--orange);font-size:26px;line-height:30px;font-weight:700;text-align:center;margin-top:10px}
.inclusions{list-style:none;margin:14px 0 0 16px;color:var(--white);font-size:9.8px;line-height:12px}
.inclusions li::before{content:"> ";color:var(--orange);font-weight:700}
.departs{text-align:center;color:var(--ink);font-size:10.5px;line-height:12px;margin-top:14px}
.front-contact{position:absolute;left:20px;top:28px;width:230px;text-align:center;font-size:13.5px;line-height:14px}
.front-contact svg{display:block;margin:0 auto 4px}
.front-contact .gap{margin-top:4px}
.brand{position:absolute;left:270px;top:84px;display:flex;align-items:center;gap:8px}
.brand-mark{width:26px;height:26px;border-radius:50%;background:var(--green)}
.brand-name{font-size:27px;font-weight:700;color:var(--ink)}
.brand-sub{position:absolute;left:380px;top:116px;font-size:11px;color:var(--ink)}

/* back page */
.back{position:absolute;left:620px;top:28px;width:545px;height:744px;background:var(--green);border-radius:0 40px 0 0}
.sheet{position:absolute;left:14px;top:18px;width:517px;height:712px;background:var(--white);border-radius:0 34px 0 34px}
.tour-head{position:absolute;left:14px;top:8px;width:268px;height:46px;background:var(--green);color:var(--gold);
  font-weight:700;font-size:11.5px;line-height:13.5px;text-align:center;padding-top:3px}
.back-contact{position:absolute;left:300px;top:9px;width:210px;color:var(--green-dark);font-weight:700;font-size:13px;line-height:14.5px}
.back-contact .row{display:flex;align-items:center;gap:6px}
.back-contact .phones{padding-left:58px;position:relative}
.back-contact .phones svg{position:absolute;left:38px;top:2px}
.about{position:absolute;left:38px;top:62px;width:460px;font-size:9.7px;line-height:12px}
.about h2{font-size:10px;color:var(--orange);font-weight:700}
.rule{position:absolute;left:14px;top:115px;width:488px;height:2px;background:var(--green)}
.itinerary{position:absolute;left:14px;top:122px;width:265px;height:460px;display:flex;flex-direction:column}
.day{flex:1;color:var(--white);font-size:7.3px;line-height:8.8px;padding:1px 4px;background:var(--green);border-bottom:1px solid var(--white)}
.day:nth-child(even){background:var(--green-light)}
.day b{display:block}
.gallery{position:absolute;left:283px;top:122px;width:201px;height:460px;display:flex;flex-direction:column;gap:4px}
.gallery div{flex:1}
.food{background:radial-gradient(circle at 40% 45%,#d9912f 0%,#a35a22 45%,#5e3317 100%)}
.fabric{background:linear-gradient(90deg,#8c2f62,#c2477a 30%,#7a4a9a 55%,#c98a44 80%,#8a2a4a)}
.bazaar{background:linear-gradient(180deg,#c8a060 0%,#c2563a 45%,#d08a3a 70%,#8a3a5a 100%)}
.monument{background:linear-gradient(180deg,#6ea6dc 0%,#bcd6ec 45%,#ecebe6 68%,#8aa872 85%,#4f7a44 100%)}
.terms{position:absolute;left:14px;top:588px;width:470px;height:78px;border:2px solid var(--green);padding:2px 4px;font-size:6.45px;line-height:7.9px}
.terms b{color:var(--orange);font-weight:400;font-size:8px}
.office{position:absolute;left:20px;top:670px;width:330px;text-align:center;font-size:10px;line-height:11.5px;color:var(--ink)}
.office strong{color:var(--gold);font-weight:700}
.back-brand{position:absolute;left:340px;top:680px;display:flex;align-items:center;gap:5px}
.back-brand .brand-mark{width:16px;height:16px}
.back-brand .brand-name{font-size:17px}
</style>
</head>
<body>

<section class="front">
  <div class="hero" role="img" aria-label="Photograph of robed monks with yellow umbrellas walking down a tree-lined path"></div>
  <h1 class="hero-title">Wander India<br>Fabric &amp; Flavour Journey</h1>

  <p class="intro"><em>India</em> is one the most captivating countries on earth - from it's rich culture to breathing scenery. A trip to <em>India</em> will create memories to last you a life time</p>

  <div class="front-foot">
    <div class="front-contact">
      <svg width="18" height="16" viewBox="0 0 18 16"><path d="M2 5c0-3 14-3 14 0v2h-4V5H6v2H2z" fill="#1c1c1c"/><rect x="4" y="8" width="10" height="7" rx="1" fill="#1c1c1c"/><circle cx="9" cy="11.5" r="2" fill="#fff"/></svg>
      09 358 6172<br>021637294
      <svg class="gap" width="16" height="12" viewBox="0 0 16 12"><rect width="16" height="12" fill="#1c1c1c"/><path d="M0 0l8 7 8-7" fill="none" stroke="#fff" stroke-width="1.3"/></svg>
      maren@kiwitripagents.example.nz<br>www.kiwitripagents.example.nz
    </div>
    <div class="brand"><span class="brand-mark"></span><span class="brand-name">KiwiTrip Agents</span></div>
    <div class="brand-sub">Maren Thistle</div>
  </div>

  <div class="offer">
    <p class="price">$6995* pp</p>
    <ul class="inclusions">
      <li>16 days fully escorted</li>
      <li>Breakfast &amp; Dinner included for 15days</li>
      <li>One Bottle of Mineral water per person per day</li>
      <li>All assistance and transfers</li>
      <li>All current taxes</li>
      <li>Culinary delight tour in Lucknow</li>
      <li>Rickshaw ride in Delhi.</li>
      <li>Accommodation with private facilities</li>
    </ul>
    <p class="departs">Tour Departs Auckland<br>15th March 2015</p>
  </div>
</section>

<section class="back">
  <div class="sheet">
    <div class="tour-head">TEXTILE AND SHOPPING TOUR OF INDIA<br>16 Days / 15 Nights<br>Escorted by Maren Thistle</div>
    <div class="back-contact">
      <div class="phones"><svg width="18" height="16" viewBox="0 0 18 16"><path d="M2 5c0-3 14-3 14 0v2h-4V5H6v2H2z" fill="#1f9a3c"/><rect x="4" y="8" width="10" height="7" rx="1" fill="#1f9a3c"/><circle cx="9" cy="11.5" r="2" fill="#fff"/></svg>09 358 6172<br>021637294</div>
      <div class="row"><svg width="16" height="12" viewBox="0 0 16 12"><rect width="16" height="12" fill="#1f9a3c"/><path d="M0 0l8 7 8-7" fill="none" stroke="#fff" stroke-width="1.3"/></svg>maren@kiwitripagents.example.nz</div>
    </div>

    <div class="about">
      <h2>About your Tour Manager: Maren Thistle</h2>
      <p>Maren has escorted many tours around India and has a passion for the culture and the people.<br>Maren also has a business in New Zealand which deals with Rajastani &amp; South India business's on a regular basis.</p>
    </div>
    <div class="rule"></div>

    <div class="itinerary">
      <div class="day"><b>Day 01: Arrive Delhi</b>A transfer to the hotel . You will receive a traditional welcome with Garland and Tilak while the hotel formalities are completed. Stay two nights in Delhi</div>
      <div class="day"><b>Day 02: In Delhi</b>Tour of Old and New Delhi. Rickshaw ride in Delhi. Also visit Humayun's Tomb</div>
      <div class="day"><b>Day 03: Delhi – Lucknow</b>Transfer to Delhi airport to board flight to Lucknow. Explore the beautiful bazaar which is famous for textiles. Stay two nights in Lucknow</div>
      <div class="day"><b>Day 04: Lucknow</b>We visit a Chikan workshop and watch skilled karigars (workers). Later, you will see some of the highlights of the city Bada Imambara</div>
      <div class="day"><b>Day 05: Lucknow – Varanasi</b>Visiting the city and the bazaar. Evening enjoy a heritage walk of the city &amp; witness grand prayer ceremony on the ghats of river Ganges</div>
      <div class="day"><b>Day 06: Varanasi – Agra</b>Boat ride on river Ganges and an excursion to Sarnath. Later in the evening transfer to the railway station in time to board overnight train to Agra</div>
      <div class="day"><b>Day 07: Arrive Agra</b>Morning arrive Agra, transfer to the hotel.Morning free to freshen up. Afternoon visit Mehtab Bagh</div>
      <div class="day"><b>Day 08: Agra</b>Visit to the Taj Mahal, tour of the Agra and the evening explore the colour bazaar of Agra famous souvenirs made out of marble</div>
      <div class="day"><b>Day 09: Agra – Jaipur</b>Travel towards Jaipur the Pink City of India. In rest of the day at leisure to explore the colour bazaar of Jaipur for textile, junk jewellery, carpet</div>
      <div class="day"><b>Day 10: Jaipur</b>Visit Amber Fort and rest of the evening is free for shopping</div>
      <div class="day"><b>Day 11: Jaipur</b>Take a full day excursion to Sanganer. See for yourself the way in which they prepare the textiles</div>
      <div class="day"><b>Day 12: Jaipur – Jodhpur</b>Travel to Jodhpur. In the evening visit Sadar Bazaar, one of the largest markets of Indian Spices and textile</div>
      <div class="day"><b>Day 13: Jodhpur</b>Sightseeing tour and visit Mehrangarh Fort. Also visit Jaswant Thada. Rest of the evening is free to enjoy shopping. Overnight at hotel</div>
      <div class="day"><b>Day 14: Jodhpur – Ranakpur – Udaipur</b>We visit Ranakpur. Stay two nights in Udaipur</div>
      <div class="day"><b>Day 15: Udaipur</b>Enjoy city tour of Udaipur, enjoy rest of the day on the banks of the Lake Pichola. Shopping at the local markets</div>
      <div class="day"><b>Day 16: Udaipur – Mumbai</b>There is a separate option should you wish to stay and explore Mumbai for a few days. Please advise at time of confirmation</div>
    </div>

    <div class="gallery">
      <div class="food" role="img" aria-label="Photograph of Indian curries, rice and breads in bowls"></div>
      <div class="fabric" role="img" aria-label="Photograph of colourful silk saris and textiles on display"></div>
      <div class="bazaar" role="img" aria-label="Photograph of a market stall piled with coloured spice powders"></div>
      <div class="monument" role="img" aria-label="Photograph of the Taj Mahal with its reflecting pool"></div>
    </div>

    <div class="terms"><b>Terms &amp; Conditions:</b> The price quoted for the land, airfare and taxes are subject to change without notice until final payment has been received in full and tickets are issued. Prices quoted are for Twin share basis. Prices correct as at 20August 2014. Deposit is non refundable and due within 7 days of the invoice dates (unless otherwise stated) Deposit required is $500 per person. Receiving confirmation of the booking means you and you have read and agreed on KiwiTrip Agents booking conditions attached. Due to any unforeseen circumstances booking conditions may change without notice hence please request a copy before making reservation. No early check-in or late check-out is included. Activities mentioned above are subject to availability. Driving time mentioned in the itinerary is approximately and is for guidance only. Travelling may take much more time than mentioned in the itinerary as it vary according to season, area of your tour and road conditions or the region. Every hotel is different in room size, services, location, category and decor. We take utmost care while selecting and suggestion hotels so every traveller can have comfortable stay.</div>

    <div class="office"><strong>TCANZ Approved Travel Broker for KiwiTrip Agents:</strong><br>Level 4, Quorn Plaza House, 3-21 Bellamy Rd,<br>Palmerston North 4410</div>
    <div class="back-brand"><span class="brand-mark"></span><span class="brand-name">KiwiTrip Agents</span></div>
  </div>
</section>

</body>
</html>
```